Corporate Travel Technology Company needs new Business Card design

We need a new business card design to reflect our re-branded company. Our company is called vendaXo (pronounced eureka) and we provide Business Intelligence and mobile travel management solutions for the corporate travel industry. Our multinational customers use our solutions to manage large travel budgets and frequent travellers, as well as to save money and reduce risk. We'd like to see designs that use the blue and green palette as well as our corporate logo (attached below). The design should communicate innovation, insight, forward thinking, contemporary, trusted.

Target Market(s)

Large multinational corporates and Travel Agencies.

Industry/Entity Type

Business

Contact Information for Business Card

Marguerite Tallis
Chief Executive
vendaXo
Phone number - +61 (0)2 8147 3092
Email address - marguerite.tallis@vendaxo.example
Mobile number - +61 (0)455 206 718
www.vendaxo.example

Font styles to use
Other font styles liked:
• Please use font as close to corporate logo as possible

Colors
0255a3
0393ce
00a990
33b8a4
33a6d7
3176b5

Requirements
Must have
• Please include the words;
• Mobile Travel Management
• Accelerating Travel Business Insights
• Use corporate logo - although icon can be stylised if needed

```html
<!DOCTYPE html>
<html lang="en">
<head>
<meta charset="utf-8">
<title>vendaXo business card</title>
<link href="https://fonts.googleapis.com/css2?family=Open+Sans:wght@400;600&display=swap" rel="stylesheet">
<style>
  :root {
    --stage: #3b3532;
    --card: #1b1c1e;
    --card-edge: #121314;
    --accent: #12a6e3;
    --green: #00a990;
    --green-soft: #33b8a4;
    --text-light: #e6e8ea;
    --text-soft: #c9cdd0;
    --decor-blue: #1d4a63;
    --decor-green: #17574f;
  }
  * { margin: 0; padding: 0; box-sizing: border-box; }
  html, body {
    width: 1200px; height: 780px; overflow: hidden;
    background: var(--stage);
    font-family: "Open Sans", Arial, sans-serif;
  }
  .stage {
    width: 1200px; height: 780px;
    display: flex; align-items: center; justify-content: center; gap: 48px;
  }
  .card {
    position: relative;
    width: 536px; height: 306px;
    background: var(--card);
    box-shadow: 0 10px 24px rgba(0,0,0,.45), 0 0 0 1px var(--card-edge);
    overflow: hidden;
  }
  .decor-ring { position: absolute; }
  .card-front .decor-ring { width: 230px; height: 230px; right: -40px; bottom: -110px; }
  .card-back .decor-ring { width: 280px; height: 280px; right: -150px; bottom: -20px; }

  .brand {
    position: absolute;
    display: flex; align-items: center; gap: 10px;
    color: var(--accent);
    font-weight: 600;
    letter-spacing: -0.5px;
    line-height: 1;
  }
  .brand-dot { border-radius: 50%; background: var(--accent); flex: none; }
  .card-front .brand { left: 34px; top: 40px; font-size: 48px; }
  .card-front .brand-dot { width: 22px; height: 22px; }
  .card-back .brand { left: 60px; top: 112px; font-size: 64px; }
  .card-back .brand-dot { width: 26px; height: 26px; }

  .tagline {
    position: absolute;
    color: var(--green-soft);
    font-size: 12px; font-weight: 600;
    letter-spacing: 1.6px; text-transform: uppercase;
  }
  .card-front .tagline { left: 34px; bottom: 26px; }
  .card-back .tagline { left: 62px; top: 198px; font-size: 13px; letter-spacing: 1.2px; }
  .tagline-rule {
    position: absolute; height: 2px; background: var(--green);
  }
  .card-back .tagline-rule { left: 62px; top: 190px; width: 48px; }

  .contact-list {
    position: absolute; left: 34px; top: 138px;
    list-style: none;
    font-size: 14px; color: var(--text-light);
  }
  .contact-list li { display: flex; align-items: center; gap: 12px; height: 24px; }
  .contact-icon {
    width: 11px; height: 11px; background: var(--accent);
    display: flex; align-items: center; justify-content: center;
  }
  .contact-icon svg { width: 7px; height: 7px; }

  .person { position: absolute; left: 316px; top: 106px; }
  .person-name { color: var(--accent); font-size: 20px; font-weight: 400; }
  .person-role { color: var(--text-soft); font-size: 14px; margin-top: 2px; }
</style>
</head>
<body>
<svg width="0" height="0" style="position:absolute" aria-hidden="true">
  <defs>
    <linearGradient id="ring-fade" x1="0" y1="0" x2="1" y2="1">
      <stop offset="0" stop-color="#1d4a63"/>
      <stop offset="1" stop-color="#17574f"/>
    </linearGradient>
  </defs>
</svg>
<main class="stage">
  <section class="card card-front">
    <svg class="decor-ring" viewBox="0 0 100 100" role="img" aria-label="Large faint brand emblem"><circle cx="50" cy="50" r="44" fill="none" stroke="url(#ring-fade)" stroke-width="11"/></svg>
    <div class="brand"><span>vendaXo</span><span class="brand-dot"></span></div>
    <ul class="contact-list">
      <li><span class="contact-icon"><svg viewBox="0 0 10 10"><circle cx="5" cy="5" r="4" fill="none" stroke="#1b1c1e" stroke-width="1.5"/></svg></span>www.vendaxo.example</li>
      <li><span class="contact-icon"><svg viewBox="0 0 10 10"><path d="M2 1h2l1 2-1 1a5 5 0 0 0 2 2l1-1 2 1v2a1 1 0 0 1-1 1A7 7 0 0 1 1 2a1 1 0 0 1 1-1z" fill="#1b1c1e"/></svg></span>+61 (0)2 8147 3092</li>
      <li><span class="contact-icon"><svg viewBox="0 0 10 10"><rect x="3" y="1" width="4" height="8" rx="1" fill="#1b1c1e"/></svg></span>+61 (0)455 206 718</li>
      <li><span class="contact-icon"><svg viewBox="0 0 10 10"><rect x="1" y="2.5" width="8" height="5" fill="none" stroke="#1b1c1e" stroke-width="1.3"/><path d="M1 2.5l4 3 4-3" fill="none" stroke="#1b1c1e" stroke-width="1.1"/></svg></span>marguerite.tallis@vendaxo.example</li>
    </ul>
    <div class="person">
      <p class="person-name">Marguerite Tallis</p>
      <p class="person-role">Chief Executive</p>
    </div>
    <p class="tagline">Mobile Travel Management</p>
  </section>

  <section class="card card-back">
    <svg class="decor-ring" viewBox="0 0 100 100" role="img" aria-label="Large faint brand emblem"><circle cx="50" cy="50" r="42" fill="none" stroke="url(#ring-fade)" stroke-width="14"/></svg>
    <div class="brand"><span>vendaXo</span><span class="brand-dot"></span></div>
    <div class="tagline-rule"></div>
    <p class="tagline">Accelerating Travel Business Insights</p>
  </section>
</main>
</body>
</html>
```